Vantrell Law Letterhead

We need a new letterhead design for a Law Firm. The address for the law firm is 4817 Larkspur Boulevard, Suite 250, Houston, Texas 77342. Phone Number: 832-619-3057; Fax Number: 832-407-1694. The logo is uploaded to the project.

```html
<!DOCTYPE html>
<html lang="en">
<head>
<meta charset="utf-8">
<title>Vantrell Law Letterhead</title>
<link href="https://fonts.googleapis.com/css2?family=Raleway:wght@400;500;700&family=Tinos&display=swap" rel="stylesheet">
<style>
  :root {
    --backdrop: #ebe3d6;
    --paper: #ffffff;
    --brand-red: #e31c24;
    --brand-navy: #1f3466;
    --ink: #2a2a2a;
    --ink-soft: #6a6a6a;
    --signature-tone: #d9d9de;
  }
  * { margin: 0; padding: 0; box-sizing: border-box; }
  html, body {
    width: 1200px; height: 1200px; overflow: hidden;
    background: var(--backdrop);
  }
  .letterhead {
    position: absolute; left: 175px; top: 50px;
    width: 850px; height: 1100px;
    background: var(--paper);
    box-shadow: 0 4px 14px rgba(0,0,0,0.12);
    overflow: hidden;
    font-family: "Raleway", sans-serif;
    color: var(--ink);
  }
  .letterhead__frame { position: absolute; inset: 0; width: 850px; height: 1100px; }
  .brand {
    position: absolute; left: 300px; top: 130px;
    display: flex; align-items: center; gap: 16px;
  }
  .brand__mark { width: 46px; height: 46px; background: var(--brand-navy); }
  .brand__name {
    font-family: "Tinos", serif; font-size: 44px;
    color: var(--brand-navy); letter-spacing: 1px; font-weight: 400;
  }
  .sender {
    position: absolute; left: 90px; top: 292px;
    font-size: 11.5px; line-height: 1.35; font-style: normal;
  }
  .sender strong { font-weight: 700; display: block; }
  .sender__phone { color: var(--ink-soft); font-size: 14px; }
  .letter {
    position: absolute; left: 235px; top: 350px; width: 520px;
    font-size: 12.5px; line-height: 1.62; text-align: justify;
  }
  .letter__salutation { font-weight: 700; margin-bottom: 18px; }
  .letter p { margin-bottom: 28px; }
  .signoff { margin-top: 6px; font-size: 12px; line-height: 1.35; }
  .signoff__name { font-weight: 700; }
  .signoff__signature {
    width: 130px; height: 52px; margin: 14px 0 0 60px;
    background: var(--signature-tone); border-radius: 4px;
  }
  .footer-contact {
    position: absolute; left: 232px; bottom: 44px;
    font-family: "Tinos", serif; font-size: 13.5px; color: var(--brand-navy);
    display: flex; gap: 22px; white-space: nowrap;
  }
</style>
</head>
<body>
  <main class="letterhead">
    <svg class="letterhead__frame" viewBox="0 0 850 1100" aria-hidden="true">
      <polygon points="0,0 850,0 850,150 725,22 0,22" fill="var(--brand-red)"/>
      <polygon points="0,945 0,1100 850,1100 850,1078 205,1078" fill="var(--brand-navy)"/>
    </svg>

    <header class="brand">
      <span class="brand__mark"></span>
      <span class="brand__name">Vantrell Law</span>
    </header>

    <address class="sender">
      <strong>1148 Meadowlark Lane</strong>
      <strong>Los Angeles, CA 90021</strong>
      <span class="sender__phone">714-305-6619</span>
    </address>

    <article class="letter">
      <p class="letter__salutation">Dear Mr. Delacroix</p>
      <p>Fusce scelerisque sem sem, non interdum ligula gravida id. Curabitur sit amet molestie elit. Pellentesque ac congue diam. Duis varius suscipit elementum. Ut ac volutpat arcu, id commodo erat. Suspendisse tempor diam ut nunc egestas finibus. Maecenas quis porttitor dolor, a accumsan odio. Phasellus nisl metus, consectetur ut venenatis sit amet, imperdiet at nunc.</p>
      <p>Donec facilisis malesuada ipsum sit amet vulputate. Integer justo justo, fermentum vitae pellentesque feugiat, ullamcorper non velit. Suspendisse molestie volutpat nisl at faucibus. Praesent posuere sodales libero, sed lacinia lacus ultrices eu. Phasellus lobortis, lectus sit amet vehicula hendrerit, risus purus blandit nunc, porttitor dictum arcu nisl varius ipsum. Nam tempus et purus sit amet cursus. Ut nec mauris quam. Integer condimentum quis magna id tempus. Pellentesque et orci scelerisque nisi faucibus egestas et at orci. Aliquam placerat ultricies erat id tincidunt. Nunc quis justo ipsum. Pellentesque at nisl et nulla posuere sollicitudin vitae vel ex. Vivamus fermentum orci sem. Phasellus tempor, metus vitae rutrum varius, ex libero mattis sapien, nec dictum enim augue non augue. Vestibulum in orci ut augue iaculis porttitor.</p>
      <p>Praesent sit amet augue auctor, ultrices dui eget, pellentesque enim. Vivamus eu elementum odio. Nulla vitae enim porta, posuere tellus in, euismod nulla. Pellentesque vitae sodales ligula, vitae viverra nunc. Integer tristique sit amet leo vel feugiat.</p>
      <div class="signoff">
        <div class="signoff__name">Marcus T. Ellery</div>
        <div>Marketing Manager</div>
        <div class="signoff__signature" role="img" aria-label="Handwritten signature"></div>
      </div>
    </article>

    <footer class="footer-contact">
      <span>4817 Larkspur Boulevard, Suite 250, Houston, Texas 77342</span>
      <span>Tel: 832-619-3057</span>
      <span>Fax: 832-407-1694</span>
    </footer>
  </main>
</body>
</html>
```